Tin Lantern Photo Booths

Im in need of business cards with a logo for my new Photo Booth business. The company will be called: Tin Lanterns Photo Booth.

Website: www.tinlanternphotobooths.example
Phone#: 555.274.0619
Bullet Points: Weddings, Charity Events, Private Parties, Corporate Parties,

Please make the logo fun. I like a clean look that and something that is very attention grabbing.

The photo booth will be setup for customers to come inside and have their pictures taken.

Good luck and have fun with it.

```html
<!DOCTYPE html>
<html lang="en">
<head>
<meta charset="utf-8">
<title>Tin Lantern Photo Booth — Business Card</title>
<link rel="stylesheet" href="https://fonts.googleapis.com/css2?family=Questrial&display=swap">
<style>
  :root {
    --brand-red: #c01f2f;
    --brand-orange: #f7941d;
    --card-white: #ffffff;
    --card-edge: #231f20;
    --label-grey: #9a9a9a;
    --page-bg: #ffffff;
  }
  * { box-sizing: border-box; margin: 0; padding: 0; }
  html, body {
    width: 868px; height: 1200px; overflow: hidden;
    background: var(--page-bg);
    font-family: "Questrial", "Century Gothic", sans-serif;
  }
  .sheet { position: relative; width: 868px; height: 1200px; }

  .card {
    position: absolute; left: 50px; width: 780px; height: 448px;
    border: 4px solid var(--card-edge);
  }
  .card--front { top: 40px; background: var(--card-white); }
  .card--back { top: 634px; background: var(--brand-red); }

  .side-label {
    position: absolute; left: 0; width: 100%; text-align: center;
    color: var(--label-grey); font-size: 36px;
  }
  .side-label--front { top: 516px; }
  .side-label--back { top: 1110px; }

  /* Front */
  .brand {
    position: absolute; left: 84px; top: 100px;
    display: flex; align-items: center; gap: 36px;
  }
  .brand__dot {
    width: 150px; height: 150px; border-radius: 50%;
    background: var(--brand-orange); flex: none;
  }
  .brand__name { color: var(--brand-red); line-height: 1; }
  .brand__line1 { display: block; font-size: 78px; letter-spacing: -1px; }
  .brand__line2 { display: block; font-size: 44px; letter-spacing: 7px; margin-top: 14px; }

  .services {
    position: absolute; left: 54px; top: 314px;
    list-style: none; display: flex; gap: 14px;
    font-size: 23px; color: var(--brand-red);
  }
  .services li::before {
    content: "•"; color: var(--brand-orange); margin-right: 8px;
  }

  /* Back */
  .back-mark {
    position: absolute; left: 50%; top: 60px; transform: translateX(-50%);
    width: 190px; height: 190px; border-radius: 50%;
    background: var(--card-white);
  }
  .back-name {
    position: absolute; left: 0; width: 100%; top: 276px;
    text-align: center; color: var(--card-white); font-size: 34px; letter-spacing: 2px;
  }
  .contact {
    position: absolute; left: 0; width: 100%; top: 352px;
    text-align: center; color: var(--card-white); font-size: 26px; line-height: 32px;
  }
</style>
</head>
<body>
  <main class="sheet">
    <section class="card card--front" aria-label="Card front">
      <div class="brand">
        <span class="brand__dot" aria-hidden="true"></span>
        <h1 class="brand__name">
          <span class="brand__line1">Tin Lantern</span>
          <span class="brand__line2">Photo Booth</span>
        </h1>
      </div>
      <ul class="services">
        <li>Weddings</li>
        <li>Charity Events</li>
        <li>Private Parties</li>
        <li>Corporate Parties</li>
      </ul>
    </section>
    <p class="side-label side-label--front">Front</p>

    <section class="card card--back" aria-label="Card back">
      <span class="back-mark" aria-hidden="true"></span>
      <p class="back-name">Tin Lantern Photo Booth</p>
      <p class="contact">Phone no. 555 274 0619<br>www.tinlanternphotobooths.example</p>
    </section>
    <p class="side-label side-label--back">Back</p>
  </main>
</body>
</html>
```